BrightPine Real Estate Sign

We are in the process of rebranding our business and need a new For Sale \ Sold sign.
We're a prestige real estate agency and therefore require a really stylish sign.
I've uploaded the following files
1. The new company logo
2. "sample sign.jpg" which shows the type of sign we would like. It is a metal sign with a top panel and bottom panel.
3. Our previous sign "previous sign.jpg" if you're interested in seeing it.
The sign must be black with white text.
Our thoughts are that the top panel (refer to sample sign) would contain the text "For Sale" or "Sold". These would be two separate panels which are interchangeable and could be screwed in place.
The bottom panel would not contain any photos like the sample. However, it may contain our logo and my contact details etc.
The sign is 900mm wide x 1200mm high.
My details are:
Name: Gareth Wimble
Web: www.bprealestate.com.au
Email: sales@bprealestate.com.au
Phone: 0491 650 387

```html
<!DOCTYPE html>
<html lang="en">
<head>
<meta charset="utf-8">
<title>BrightPine Real Estate – For Sale / Sold Signs</title>
<link rel="stylesheet" href="https://fonts.googleapis.com/css2?family=Arimo:wght@700&family=Tinos:wght@700&display=swap">
<style>
  :root {
    --sign-black: #000000;
    --sign-white: #ffffff;
    --gap-white: #ffffff;
  }
  * { box-sizing: border-box; margin: 0; padding: 0; }
  html, body {
    width: 1200px;
    height: 791px;
    overflow: hidden;
    background: var(--gap-white);
  }
  .sign-set {
    position: relative;
    width: 1200px;
    height: 791px;
    background: var(--gap-white);
  }
  .sign {
    position: absolute;
    top: 0;
    width: 594px;
    height: 791px;
    background: var(--sign-black);
    color: var(--sign-white);
  }
  .sign--for-sale { left: 0; }
  .sign--sold { left: 606px; }

  .brand {
    position: absolute;
    top: 58px;
    left: 0;
    right: 0;
    display: flex;
    justify-content: center;
    align-items: center;
    gap: 18px;
  }
  .brand__square {
    width: 46px;
    height: 46px;
    background: var(--sign-white);
  }
  .brand__name {
    font-family: "Arimo", Arial, sans-serif;
    font-weight: 700;
    font-size: 34px;
    letter-spacing: 0.5px;
    color: var(--sign-white);
    white-space: nowrap;
  }

  .status-band {
    position: absolute;
    top: 302px;
    left: 0;
    width: 594px;
    height: 186px;
    background: var(--sign-white);
    display: flex;
    align-items: center;
    justify-content: center;
  }
  .sign--sold .status-band { left: -12px; width: 606px; padding-left: 12px; }
  .status-band__label {
    font-family: "Arimo", Arial, sans-serif;
    font-weight: 700;
    color: var(--sign-black);
    line-height: 1;
    white-space: nowrap;
  }
  .status-band__label--for-sale { font-size: 92px; letter-spacing: 3px; margin-top: 4px; }
  .status-band__label--sold { font-size: 142px; letter-spacing: 4px; margin-top: 6px; }

  .agent {
    position: absolute;
    left: 15px;
    right: 12px;
    top: 648px;
    font-family: "Tinos", "Times New Roman", serif;
    font-weight: 700;
    color: var(--sign-white);
  }
  .agent__name { font-size: 30px; line-height: 38px; }
  .agent__phone { font-size: 30px; line-height: 42px; letter-spacing: 0.5px; }
  .agent__links {
    display: flex;
    justify-content: space-between;
    font-size: 16.5px;
    line-height: 26px;
    white-space: nowrap;
  }
</style>
</head>
<body>
  <main class="sign-set">
    <section class="sign sign--for-sale" aria-label="For Sale sign">
      <div class="brand">
        <span class="brand__square" aria-hidden="true"></span>
        <span class="brand__name">BrightPine Real Estate</span>
      </div>
      <div class="status-band">
        <span class="status-band__label status-band__label--for-sale">FOR SALE</span>
      </div>
      <div class="agent">
        <p class="agent__name">Gareth Wimble</p>
        <p class="agent__phone">0491 650 387</p>
        <p class="agent__links">
          <span>Web: www.bprealestate.com.au</span>
          <span>Email: sales@bprealestate.com.au</span>
        </p>
      </div>
    </section>

    <section class="sign sign--sold" aria-label="Sold sign">
      <div class="brand">
        <span class="brand__square" aria-hidden="true"></span>
        <span class="brand__name">BrightPine Real Estate</span>
      </div>
      <div class="status-band">
        <span class="status-band__label status-band__label--sold">SOLD</span>
      </div>
      <div class="agent">
        <p class="agent__name">Gareth Wimble</p>
        <p class="agent__phone">0491 650 387</p>
        <p class="agent__links">
          <span>Web: www.bprealestate.com.au</span>
          <span>Email: sales@bprealestate.com.au</span>
        </p>
      </div>
    </section>
  </main>
</body>
</html>
```